Medida Certa - Working hours register App needs interface design

Medida Certa, a 1 million users Brazilian website focused on general calculations needs an interface to an App for registering the working hours of a housemaid, a nanny, a housekeeper or other domestic workers.
The final users should be mainly housewifes.
The wireframe of the pages is in the LarPonto_layout.xls file attached.
Logo is also available in the wireframe.
The interface should be optimized for Android on Orbita KX with a 5'' screen.
Target Market(s)
Females, educated, from 30 to 50 y.o.
Industry/Entity Type
Android
Look and feel
Each slider illustrates characteristics of the customer's brand and the style your logo design should communicate.

```html
<!DOCTYPE html>
<html lang="en">
<head>
<meta charset="utf-8">
<title>Medida Certa – LarPonto</title>
<link href="https://fonts.googleapis.com/css2?family=Ubuntu:wght@300;400;500;700&display=swap" rel="stylesheet">
<style>
  :root{
    --band-top:#4e4e4e;
    --band-bottom:#151515;
    --page:#e9e7e6;
    --page-low:#f1f1f1;
    --ink:#2b2b2b;
    --ink-soft:#3e3e3e;
    --name:#3b4049;
    --muted:#7a7a7a;
    --red:#e0161b;
    --red-dark:#b80d12;
    --row-top:#f7f7f7;
    --row-bottom:#d9d9d9;
    --white:#ffffff;
  }
  *{box-sizing:border-box;margin:0;padding:0}
  html,body{width:1200px;height:720px;overflow:hidden}
  body{font-family:'Ubuntu',sans-serif;background:var(--page-low);position:relative}

  .stage-band{position:absolute;left:0;top:0;width:1200px;height:260px;
    background:linear-gradient(#3a3a3a 0%,#4c4c4c 18%,#2e2e2e 19%,var(--band-bottom) 100%)}
  .stage-mid{position:absolute;left:0;top:260px;width:1200px;height:172px;background:var(--page)}

  /* shared list parts */
  .worker-list{list-style:none;position:relative}
  .worker{display:flex;align-items:center;background:linear-gradient(var(--row-top),var(--row-bottom));border:1px solid #c4c4c4}
  .worker-photo{flex:none;align-self:stretch}
  .worker-info{flex:1;line-height:1.15;white-space:nowrap;overflow:hidden}
  .worker-name{display:block;font-weight:500;color:var(--name)}
  .worker-role{display:block;font-weight:400;color:var(--muted)}
  .worker-edit{flex:none;border-radius:2px;background:linear-gradient(#f23237,var(--red-dark));display:flex;align-items:center;justify-content:center}
  .mark{border-radius:6px;background:linear-gradient(#ee2228,var(--red-dark))}

  /* small app screen */
  .app-screen{position:absolute;left:40px;top:136px;width:230px;height:408px;background:var(--white);overflow:hidden;
    border:1px solid #999}
  .app-bar{height:48px;background:linear-gradient(#3c3c3c,#121212);display:flex;align-items:center;padding:0 9px;gap:8px}
  .app-bar .mark{width:32px;height:32px;border-radius:4px}
  .app-title{color:var(--white);line-height:1.1}
  .app-title b{display:block;font-weight:700;font-size:11px;letter-spacing:.2px}
  .app-title span{font-size:8.5px}
  .app-edit{margin-left:auto;width:15px;height:15px;border-radius:2px;background:#555;border:1px solid #999;display:flex;align-items:center;justify-content:center}
  .app-screen .worker-list{padding:10px 15px 0 9px}
  .app-screen .worker{height:40px;margin-bottom:2px}
  .app-screen .worker-photo{width:39px}
  .app-screen .worker-info{padding-left:6px}
  .app-screen .worker-name{font-size:12px}
  .app-screen .worker-role{font-size:8.5px}
  .app-screen .worker-edit{width:19px;height:19px;margin-right:0}
  .scrollbar{position:absolute;right:8px;top:10px;width:3px;height:92px;background:var(--red);border-radius:2px}

  /* brand block */
  .brand{position:absolute;left:308px;top:147px;display:flex;align-items:center;gap:20px}
  .brand .mark{width:97px;height:97px}
  .brand-name{color:var(--white);line-height:1.05}
  .brand-name b{display:block;font-size:27px;font-weight:700;letter-spacing:.4px}
  .brand-name span{font-size:23px;font-weight:400}

  .pitch{position:absolute;left:315px;top:290px;width:450px;color:var(--ink-soft)}
  .pitch h1{font-size:26px;font-weight:700;color:var(--ink);letter-spacing:.4px;margin-bottom:14px}
  .pitch .lead{font-size:16.8px;font-weight:300;line-height:1.22;width:430px;margin-left:3px;margin-bottom:43px}
  .pitch .body{font-size:11.2px;font-weight:300;line-height:1.3;width:445px;margin-left:3px}
  .store-badge{display:block;width:114px;height:36px;margin-top:14px;background:#0e0e0e;border-radius:2px;border:1px solid #555}

  /* zoomed app screen */
  .zoom-screen{position:absolute;left:834px;top:0;width:366px;height:720px;background:#f4f4f4;overflow:hidden;
    box-shadow:-6px 0 14px rgba(0,0,0,.18);border-left:1px solid #bbb}
  .zoom-bar{height:116px;background:linear-gradient(#2e2e2e,#111);display:flex;align-items:center;padding-left:26px;gap:14px;border-bottom:2px solid #ddd}
  .zoom-bar .mark{width:96px;height:96px}
  .zoom-title{color:var(--white);line-height:1.05;white-space:nowrap}
  .zoom-title b{display:block;font-size:27px;font-weight:700;letter-spacing:.4px}
  .zoom-title span{font-size:23px}
  .zoom-screen .worker-list{padding:25px 0 0 24px}
  .zoom-screen .worker{height:99px;margin-bottom:6px;border-right:none}
  .zoom-screen .worker-photo{width:99px}
  .zoom-screen .worker-info{padding-left:14px}
  .zoom-screen .worker-name{font-size:32px}
  .zoom-screen .worker-role{font-size:22px;font-weight:400;margin-top:2px}
</style>
</head>
<body>
  <div class="stage-band"></div>
  <div class="stage-mid"></div>

  <section class="app-screen">
    <header class="app-bar">
      <div class="mark"></div>
      <div class="app-title"><b>MEDIDA CERTA</b><span>LARPONTO</span></div>
      <div class="app-edit"><svg width="9" height="9" viewBox="0 0 12 12"><path d="M2 10 L2.5 7.5 L8 2 L10 4 L4.5 9.5 Z" fill="none" stroke="#fff" stroke-width="1.4"/></svg></div>
    </header>
    <ul class="worker-list">
      <li class="worker"><div class="worker-photo" role="img" aria-label="Portrait photo of Lina Maros" style="background:linear-gradient(#5a3b2e,#c89a86)"></div><div class="worker-info"><span class="worker-name">Lina Maros</span><span class="worker-role">Baby Sitter</span></div><div class="worker-edit"><svg width="11" height="11" viewBox="0 0 12 12"><rect x="1" y="2" width="8" height="9" fill="none" stroke="#fff" stroke-width="1.2"/><path d="M4 8 L4.5 6 L9.5 1 L11 2.5 L6 7.5 Z" fill="#fff"/></svg></div></li>
      <li class="worker"><div class="worker-photo" role="img" aria-label="Portrait photo of Theo Brandt" style="background:linear-gradient(#e0b090,#c8432b)"></div><div class="worker-info"><span class="worker-name">Theo Brandt</span><span class="worker-role">Web Coder</span></div><div class="worker-edit"><svg width="11" height="11" viewBox="0 0 12 12"><rect x="1" y="2" width="8" height="9" fill="none" stroke="#fff" stroke-width="1.2"/><path d="M4 8 L4.5 6 L9.5 1 L11 2.5 L6 7.5 Z" fill="#fff"/></svg></div></li>
      <li class="worker"><div class="worker-photo" role="img" aria-label="Portrait photo of Clara Voss" style="background:linear-gradient(#b07a4f,#e8c6ae)"></div><div class="worker-info"><span class="worker-name">Clara Voss</span><span class="worker-role">Cook</span></div><div class="worker-edit"><svg width="11" height="11" viewBox="0 0 12 12"><rect x="1" y="2" width="8" height="9" fill="none" stroke="#fff" stroke-width="1.2"/><path d="M4 8 L4.5 6 L9.5 1 L11 2.5 L6 7.5 Z" fill="#fff"/></svg></div></li>
      <li class="worker"><div class="worker-photo" role="img" aria-label="Portrait photo of Davi Lemos" style="background:linear-gradient(#2a211c,#9a6c55)"></div><div class="worker-info"><span class="worker-name">Davi Lemos</span><span class="worker-role">Party DJ</span></div><div class="worker-edit"><svg width="11" height="11" viewBox="0 0 12 12"><rect x="1" y="2" width="8" height="9" fill="none" stroke="#fff" stroke-width="1.2"/><path d="M4 8 L4.5 6 L9.5 1 L11 2.5 L6 7.5 Z" fill="#fff"/></svg></div></li>
      <li class="worker"><div class="worker-photo" role="img" aria-label="Portrait photo of Irene Salas" style="background:linear-gradient(#e6e2dc,#8a5a3e)"></div><div class="worker-info"><span class="worker-name">Irene Salas</span><span class="worker-role">Baby Sitter</span></div><div class="worker-edit"><svg width="11" height="11" viewBox="0 0 12 12"><rect x="1" y="2" width="8" height="9" fill="none" stroke="#fff" stroke-width="1.2"/><path d="M4 8 L4.5 6 L9.5 1 L11 2.5 L6 7.5 Z" fill="#fff"/></svg></div></li>
      <li class="worker"><div class="worker-photo" role="img" aria-label="Portrait photo of Otto Ferraz" style="background:linear-gradient(#3a3a3a,#c9a58d)"></div><div class="worker-info"><span class="worker-name">Otto Ferraz</span><span class="worker-role">Animator</span></div><div class="worker-edit"><svg width="11" height="11" viewBox="0 0 12 12"><rect x="1" y="2" width="8" height="9" fill="none" stroke="#fff" stroke-width="1.2"/><path d="M4 8 L4.5 6 L9.5 1 L11 2.5 L6 7.5 Z" fill="#fff"/></svg></div></li>
      <li class="worker"><div class="worker-photo" role="img" aria-label="Portrait photo of Rui Calder" style="background:linear-gradient(#7f7a6c,#b08a70)"></div><div class="worker-info"><span class="worker-name">Rui Calder</span><span class="worker-role">Web Developer</span></div><div class="worker-edit"><svg width="11" height="11" viewBox="0 0 12 12"><rect x="1" y="2" width="8" height="9" fill="none" stroke="#fff" stroke-width="1.2"/><path d="M4 8 L4.5 6 L9.5 1 L11 2.5 L6 7.5 Z" fill="#fff"/></svg></div></li>
      <li class="worker"><div class="worker-photo" role="img" aria-label="Portrait photo of Marta Quill" style="background:linear-gradient(#8d5a3a,#e0b79c)"></div><div class="worker-info"><span class="worker-name">Marta Quill</span><span class="worker-role">Home Maid</span></div><div class="worker-edit"><svg width="11" height="11" viewBox="0 0 12 12"><rect x="1" y="2" width="8" height="9" fill="none" stroke="#fff" stroke-width="1.2"/><path d="M4 8 L4.5 6 L9.5 1 L11 2.5 L6 7.5 Z" fill="#fff"/></svg></div></li>
      <li class="worker"><div class="worker-photo" role="img" aria-label="Portrait photo of Theo Brandt" style="background:linear-gradient(#e0b090,#c8432b)"></div><div class="worker-info"><span class="worker-name">Theo Brandt</span><span class="worker-role">Web Coder</span></div><div class="worker-edit"><svg width="11" height="11" viewBox="0 0 12 12"><rect x="1" y="2" width="8" height="9" fill="none" stroke="#fff" stroke-width="1.2"/><path d="M4 8 L4.5 6 L9.5 1 L11 2.5 L6 7.5 Z" fill="#fff"/></svg></div></li>
      <li class="scrollbar"></li>
    </ul>
  </section>

  <div class="brand">
    <div class="mark"></div>
    <div class="brand-name"><b>MEDIDA CERTA</b><span>LARPONTO</span></div>
  </div>

  <article class="pitch">
    <h1>LOREM IMPSUM</h1>
    <p class="lead">More than one million users Brazilian website focused on general calculations needs an interface to an App for registering the working hours of a housemaid, a nanny, a housekeeper or other domestic workers.</p>
    <p class="body">This is Layoutpad's version &nbsp;of Lorem Ipsum. Proin gravida nibh vel velit auctor aliquet. Aenean sollicitudin, lorem quis bibendum auctor, nisi elit consequat ipsum, nec sagittis sem nibh id elit. Duis sed odio sit amet nibh vulputate cursus a sit amet mauris. Morbi accumsan ipsum velit. Nam nec tellus a odio tincidunt auctor a ornare odio. Sed non &nbsp;mauris vitae erat consequat auctor eu in elit. Class aptent taciti sociosqu ad litora torquent per conubia nostra, per inceptos himenaeos.</p>
    <span class="store-badge" aria-label="App store badge"></span>
  </article>

  <section class="zoom-screen">
    <header class="zoom-bar">
      <div class="mark"></div>
      <div class="zoom-title"><b>MEDIDA CERTA</b><span>LARPONTO</span></div>
    </header>
    <ul class="worker-list">
      <li class="worker"><div class="worker-photo" role="img" aria-label="Portrait photo of Lina Maros" style="background:linear-gradient(#5a3b2e,#c89a86)"></div><div class="worker-info"><span class="worker-name">Lina Maros</span><span class="worker-role">Baby Sitter</span></div></li>
      <li class="worker"><div class="worker-photo" role="img" aria-label="Portrait photo of Theo Brandt" style="background:linear-gradient(#e0b090,#c8432b)"></div><div class="worker-info"><span class="worker-name">Theo Brandt</span><span class="worker-role">Web Coder</span></div></li>
      <li class="worker"><div class="worker-photo" role="img" aria-label="Portrait photo of Clara Voss" style="background:linear-gradient(#b07a4f,#e8c6ae)"></div><div class="worker-info"><span class="worker-name">Clara Voss</span><span class="worker-role">Cook</span></div></li>
      <li class="worker"><div class="worker-photo" role="img" aria-label="Portrait photo of Davi Lemos" style="background:linear-gradient(#2a211c,#9a6c55)"></div><div class="worker-info"><span class="worker-name">Davi Lemos</span><span class="worker-role">Party DJ</span></div></li>
      <li class="worker"><div class="worker-photo" role="img" aria-label="Portrait photo of Irene Salas" style="background:linear-gradient(#e6e2dc,#8a5a3e)"></div><div class="worker-info"><span class="worker-name">Irene Salas</span><span class="worker-role">Baby Sitter</span></div></li>
      <li class="worker"><div class="worker-photo" role="img" aria-label="Portrait photo of Otto Ferraz" style="background:linear-gradient(#3a3a3a,#c9a58d)"></div><div class="worker-info"><span class="worker-name">Otto Ferraz</span><span class="worker-role">Animator</span></div></li>
    </ul>
  </section>
</body>
</html>
```